Clean bold and classy business card front and back
Kwr can be the logo
My name Trent Holloman as owner
Phone email and address
Owner Trent Holloman
Phone 8505550147
Email ridgelineinsulate@mailnest.example
Address170 frank pais rd Havana fl 32399

Industry/Entity Type

Business

Contact Information for Business Card

Owner Trent Holloman
Phone 8505550147

Requirements
Must have
• Keystone wall render under Kwr logo
Nice to have
• Bold and clean. Maybe use Kwr as logo and name under it. Have logo on one side and info on the other side with logo also
• Put a pic up. It doesn't have to be that but something that can be used
• Try some fancy fonts also

```html
<!DOCTYPE html>
<html lang="en">
<head>
<meta charset="utf-8">
<title>Kwr – Keystone Wall Render Business Card</title>
<link rel="stylesheet" href="https://fonts.googleapis.com/css2?family=Open+Sans:wght@400;600;700;800&display=swap">
<style>
  :root {
    --backdrop: #3b3532;
    --card: #0d0d0d;
    --ink: #f2f2f2;
    --orange: #f07a22;
    --blue: #2a86c9;
    --silver: #c9c9c9;
  }
  * { box-sizing: border-box; margin: 0; padding: 0; }
  html, body {
    width: 1200px;
    height: 900px;
    overflow: hidden;
  }
  body {
    background: var(--backdrop);
    font-family: "Open Sans", Arial, sans-serif;
    color: var(--ink);
    position: relative;
  }
  .card {
    position: absolute;
    top: 301px;
    width: 520px;
    height: 298px;
    background: var(--card);
    border-radius: 3px;
    box-shadow: 0 10px 30px rgba(0,0,0,0.45);
  }
  .card--front { left: 60px; }
  .card--back  { left: 620px; }

  .brand {
    position: absolute;
    display: flex;
    flex-direction: column;
    line-height: 1;
  }
  .brand__name {
    display: flex;
    align-items: center;
    gap: 10px;
    font-weight: 800;
    font-size: 46px;
    letter-spacing: 0.5px;
  }
  .brand__mark {
    width: 14px;
    height: 14px;
    flex: none;
  }
  .brand__tagline {
    font-weight: 700;
    font-size: 16px;
    margin-top: 6px;
    letter-spacing: 0.3px;
  }

  .card--front .brand { left: 36px; top: 36px; }
  .card--front .brand__name { color: var(--blue); }
  .card--front .brand__mark { background: var(--blue); }
  .card--front .brand__tagline { color: var(--orange); padding-left: 24px; }

  .card--back .brand {
    left: 0;
    right: 0;
    top: 104px;
    align-items: center;
  }
  .card--back .brand__name { color: var(--silver); }
  .card--back .brand__mark { background: var(--silver); }
  .card--back .brand__tagline { color: var(--silver); }

  .contact {
    position: absolute;
    left: 200px;
    top: 132px;
    font-size: 13.5px;
  }
  .contact__name {
    color: var(--orange);
    font-weight: 600;
    font-size: 17px;
    line-height: 1.2;
  }
  .contact__role {
    color: var(--blue);
    font-size: 14px;
    margin-bottom: 14px;
  }
  .contact__line {
    display: flex;
    align-items: center;
    gap: 8px;
    line-height: 1.6;
  }
  .contact__line svg { width: 11px; height: 11px; flex: none; }
  .contact__address { margin-top: 14px; }
</style>
</head>
<body>
  <section class="card card--front" aria-label="Card front">
    <div class="brand">
      <span class="brand__name"><span class="brand__mark"></span>Kwr</span>
      <span class="brand__tagline">Keystone wall render</span>
    </div>
    <div class="contact">
      <p class="contact__name">Trent Holloman</p>
      <p class="contact__role">Owner</p>
      <p class="contact__line">
        <svg viewBox="0 0 12 12" aria-hidden="true"><path fill="#2a86c9" d="M2.4 1h2l.8 2.4-1.3.9a6.6 6.6 0 0 0 3 3l.9-1.3 2.4.8v2c0 .7-.6 1.2-1.3 1.2A8.9 8.9 0 0 1 1.2 2.3C1.2 1.6 1.7 1 2.4 1z"/></svg>
        8505550147
      </p>
      <p class="contact__line">
        <svg viewBox="0 0 12 12" aria-hidden="true"><rect x="1" y="2.5" width="10" height="7" rx="1" fill="#2a86c9"/><path d="M1.5 3l4.5 3.5L10.5 3" fill="none" stroke="#0d0d0d" stroke-width="1"/></svg>
        ridgelineinsulate@mailnest.example
      </p>
      <p class="contact__address">428 dunmore ct Havana, fl 32399</p>
    </div>
  </section>

  <section class="card card--back" aria-label="Card back">
    <div class="brand">
      <span class="brand__name"><span class="brand__mark"></span>Kwr</span>
      <span class="brand__tagline">Keystone wall render</span>
    </div>
  </section>
</body>
</html>
```